Mango Grove Indian Restaurants 2019 Menu

Hi,
Please find attached menu text in pdf format. It contains 4 pages. Please work on the menu pages. I will further work with the winner to add the cover page and images as an extended project

Please visit www.mangogroveeats.com.au for more information

```html
<!DOCTYPE html>
<html lang="en">
<head>
<meta charset="utf-8">
<title>Mango Grove Indian Restaurant – Drinks, Condiments, Salads</title>
<link rel="stylesheet" href="https://fonts.googleapis.com/css2?family=Josefin+Sans:wght@300;400;600;700&family=Oswald:wght@400;600&display=swap">
<style>
:root{
  --backdrop:#a9460c;
  --menu-red:#971528;
  --menu-red-light:#a81c31;
  --paper:#ecebe8;
  --pattern:#e3dede;
  --ink-pink:#f1c9cf;
  --ink-soft:#e7a9b2;
  --outline-pink:#e9a3ac;
  --logo-red:#8e1326;
  --ink-dark:#3a2f2f;
  --veg:#7dbb42;
  --vegan:#b36ac4;
  --gluten:#3aa6a0;
  --spicy:#f2c200;
}
*{box-sizing:border-box;margin:0;padding:0}
html,body{width:1200px;height:1075px;overflow:hidden}
body{background:var(--backdrop);font-family:"Josefin Sans",sans-serif;position:relative}
.menu-page{position:absolute;left:250px;top:42px;width:700px;height:990px;display:flex;box-shadow:0 20px 40px rgba(0,0,0,.25)}
.brand-strip{width:210px;height:100%;background:var(--paper);position:relative;overflow:hidden}
.brand-pattern{position:absolute;inset:0;background:linear-gradient(160deg,var(--paper),var(--pattern) 50%,var(--paper))}
.brand-name{position:absolute;top:48px;left:0;width:100%;text-align:center;color:var(--logo-red)}
.brand-name .lead{display:block;font-size:14px;font-weight:600;color:var(--ink-dark)}
.brand-name .name{display:block;font-size:26px;font-weight:700;line-height:1;text-transform:uppercase;margin:4px 0}
.brand-name .kind{display:block;font-size:14px;font-weight:600;color:var(--ink-dark)}
.section-title{position:absolute;left:0;top:300px;width:210px;height:420px}
.tagline{position:absolute;left:18px;bottom:26px;right:14px;font-size:10px;font-weight:600;letter-spacing:1.2px;line-height:1.4;color:var(--ink-dark);text-transform:uppercase}
.menu-list{flex:1;background:linear-gradient(180deg,var(--menu-red),var(--menu-red-light));color:var(--ink-pink);padding:34px 40px 24px 40px;display:flex;flex-direction:column}
.menu-header{text-align:center;font-family:"Oswald",sans-serif;color:var(--ink-pink);letter-spacing:2px;text-transform:uppercase;padding-bottom:16px;border-bottom:1px solid var(--ink-soft);margin:0 -40px 0 -40px}
.menu-header .small{font-size:13px;display:block}
.menu-header .large{font-size:15px;font-weight:600;display:block}
.items{flex:1;display:flex;flex-direction:column;justify-content:space-between;padding-top:18px}
.item{position:relative;padding-right:90px}
.item + .item::before{content:"";position:absolute;top:-12px;left:45%;width:70px;border-top:1px solid var(--ink-soft)}
.item-name{font-size:15px;font-weight:600;letter-spacing:.8px;text-transform:uppercase;color:#fbe3e6}
.item-desc{font-size:9.5px;font-weight:300;letter-spacing:.6px;text-transform:uppercase;line-height:1.35;margin-top:3px}
.item-options{list-style:none;margin-top:3px;font-size:9px;letter-spacing:.6px;text-transform:uppercase;line-height:1.3;font-weight:300;columns:2;width:240px}
.item-options li{white-space:nowrap}
.item-options li::before{content:"• ";color:var(--ink-pink)}
.item-meta{position:absolute;right:0;top:0;width:80px;text-align:right}
.badges{display:flex;gap:3px;justify-content:flex-end;align-items:center}
.badge{width:10px;height:10px;border-radius:50%;border:1px solid #fff}
.badge.veg{background:var(--veg)}
.badge.vegan{background:var(--vegan)}
.badge.gluten{background:var(--gluten)}
.badge.spicy{width:24px;border-radius:5px;background:var(--spicy)}
.price{display:block;font-size:12px;margin-top:4px;letter-spacing:1px}
.price-list{list-style:none;margin-top:4px;font-size:10px;letter-spacing:1px;line-height:1.3}
</style>
</head>
<body>
<main class="menu-page">
  <aside class="brand-strip">
    <div class="brand-pattern" role="img" aria-label="Faint ornamental paisley pattern in pale pink on light grey"></div>
    <div class="brand-name">
      <span class="lead">the</span>
      <span class="name">Mango<br>Grove</span>
      <span class="kind">indian restaurant</span>
    </div>
    <svg class="section-title" viewBox="0 0 210 420" aria-label="Drinks, Condiments, Salads">
      <g transform="rotate(90 105 210)" font-family="Oswald, sans-serif" font-weight="600" fill="none" stroke="var(--outline-pink)" stroke-width="1.2" text-anchor="middle" letter-spacing="3">
        <text x="105" y="150" font-size="40">DRINKS</text>
        <text x="105" y="200" font-size="40">CONDIMENTS</text>
        <text x="105" y="250" font-size="40">SALADS</text>
      </g>
    </svg>
    <p class="tagline">Your best Indian restaurant in Perth's northern suburbs</p>
  </aside>

  <section class="menu-list">
    <header class="menu-header">
      <span class="small">House Made</span>
      <span class="large">Drinks-Condiments-Salads</span>
    </header>
    <div class="items">
      <article class="item">
        <h2 class="item-name">Garden Vegetables</h2>
        <p class="item-desc">Choice of sliced garden vegetables</p>
        <ul class="item-options"><li>Carrot</li><li>Cucumber</li><li>Green chillies</li><li>Lemon</li><li>Onion</li><li>Tomato</li></ul>
        <div class="item-meta"><div class="badges"><span class="badge veg"></span><span class="badge vegan"></span><span class="badge gluten"></span></div><span class="price">$ 3</span></div>
      </article>
      <article class="item">
        <h2 class="item-name">Indian Pickles</h2>
        <p class="item-desc">Imported pickles made from a variety of vegetables and fruits, preserved in edible oil along with various exotic spices.</p>
        <ul class="item-options"><li>Chilli</li><li>Garlic</li><li>Lime</li><li>Mango</li><li>Mixed</li><li>Red chilli</li></ul>
        <div class="item-meta"><div class="badges"><span class="badge vegan"></span><span class="badge gluten"></span><span class="badge veg"></span></div><span class="price">$ 3</span></div>
      </article>
      <article class="item">
        <h2 class="item-name">Lassi</h2>
        <p class="item-desc">Traditional drink made from blend of yogurt, water, spices and sometimes fruit.</p>
        <ul class="item-options"><li>Mango</li><li>Masala</li><li>Salted</li><li>Sweet</li></ul>
        <div class="item-meta"><div class="badges"><span class="badge gluten"></span><span class="badge veg"></span></div>
          <ul class="price-list"><li>$ 4</li><li>$ 4</li><li>$ 4</li><li>$ 3</li></ul></div>
      </article>
      <article class="item">
        <h2 class="item-name">Mint &amp; Coriander Chutney</h2>
        <p class="item-desc">Fresh mint and coriander blended with green chillies, ginger, yoghurt topped with freshly squeezed lemon juice.</p>
        <div class="item-meta"><div class="badges"><span class="badge spicy"></span><span class="badge gluten"></span><span class="badge veg"></span></div><span class="price">$ 3</span></div>
      </article>
      <article class="item">
        <h2 class="item-name">Papadum</h2>
        <p class="item-desc">A deep fried, thin, crisp flatbread made from peeled black gram flour, rice flour and salt.</p>
        <div class="item-meta"><div class="badges"><span class="badge vegan"></span><span class="badge gluten"></span><span class="badge veg"></span></div><span class="price">$ 3</span></div>
      </article>
      <article class="item">
        <h2 class="item-name">Raitha</h2>
        <p class="item-desc">A condiment prepared from whisked yoghurt with thinly diced raw vegetables – cucumber, red onion, tomato and a pinch of salt.</p>
        <div class="item-meta"><div class="badges"><span class="badge gluten"></span><span class="badge veg"></span></div><span class="price">$ 5</span></div>
      </article>
      <article class="item">
        <h2 class="item-name">Tamarind &amp; Date Chutney</h2>
        <p class="item-desc">A sweet, spicy and tangy condiment prepared from tamarind, dates, cane sugar, ginger and exotic spices.</p>
        <div class="item-meta"><div class="badges"><span class="badge spicy"></span><span class="badge vegan"></span><span class="badge gluten"></span><span class="badge veg"></span></div><span class="price">$ 3</span></div>
      </article>
    </div>
  </section>
</main>
</body>
</html>
```